KLD Photography Editing & Support Services for Real Estate

We require a double sided A4 flyer to promote our photography services to real estate agencies.
This particular service is targeted to rural areas where reliable, professional and highly skilled photographers are difficult to source. We teach the agent how to photograph, they upload files to a server and we take care of the rest (image editing, quality control and delivery). This will give the agents flexibility with when to shoot and eliminates the stress of managing a photographer / contractor. We offer a 1 day face to face training session and competitive packages for equipment start up.
We would like the flyer to look clean & very professional. The flyer should showcase samples of our work to highlight what can be achieved by using our services. We like the look of a black or dark background behind the text and feel that would look nice with our photographs provided. Otherwise open to your suggestions and ideas.
TEXT FOR FLYER:
Welcome to the KLD Real Estate Photography Editing and Support Service
• Take your real estate business to the next level by providing impressive real estate imagery that makes you stands out from the competition
• Omit the stress of trying to find a good photographer or managing an unreliable one and hence have more time to focus on other aspects of your business
• Showcase your listings with better quality and more impactful photographs than your competitors thereby increasing potential for a quick sale
• Great first impressions matter and you will achieve this by looking and feeling more professional. This will attract and retain more future clients.
HOW IT WORKS
• We understand that your time is valuable, so let us handle the editing and delivery of your images. You shoot, and we take care of the rest.
• Images are edited and delivered within 1 working day
INCLUSIONS:
• Full day face to face training (we come to you) and instructional handbook
• We will teach you everything you need to know about your equipment and how to take stunning real estate photographs
• Service turnaround within 1 working day
• Free HELP desk service Mon-Fri
• 12 month Exclusivity (rural towns only) for a limited time
INVESTMENT
• 99 per listing for us to manage images including editing, quality control and delivery (10 Images)
• Ask us about competitive packages for photography equipment if required
SUMMARY
The KLD Real Estate Photography Editing and Support Service is the perfect solution for busy real estate professionals who want to take their business to the next level. Our service is affordable, flexible, and designed to help you showcase your listings in the best possible light.
Contact us today to learn more about how we can help you.

```html
<!DOCTYPE html>
<html lang="en">
<head>
<meta charset="utf-8">
<title>KLD Real Estate Photography Editing and Support Service – Flyer</title>
<link href="https://fonts.googleapis.com/css2?family=Cinzel:wght@500;700&family=Montserrat:wght@300;400;500&display=swap" rel="stylesheet">
<style>
  :root{
    --canvas:#ffffff;
    --ink:#141414;
    --panel:#1b1b1b;
    --text:#f2f2f2;
    --muted:#9a9a9a;
    --rule:#5a5a5a;
    --tab:#6f6f6f;
    --box:#e9e9e9;
    --box-text:#2a2a2a;
  }
  *{box-sizing:border-box;margin:0;padding:0}
  html,body{width:881px;height:1200px;overflow:hidden;background:var(--canvas)}
  .spread{position:relative;width:881px;height:1200px}
  .page{position:absolute;top:303px;width:420px;height:594px;background:var(--ink);overflow:hidden;
    box-shadow:6px 8px 10px rgba(0,0,0,.35);font-family:"Montserrat",sans-serif;color:var(--text)}
  .page--front{left:13px}
  .page--back{left:448px}
  .collage{position:absolute;left:0;top:0;display:block}
  .brand{position:absolute;left:14px;top:16px;width:150px;text-align:center}
  .brand-name{font-family:"Montserrat",sans-serif;font-weight:300;font-size:10.5px;letter-spacing:3.4px;color:var(--muted);text-transform:uppercase}
  .brand-role{font-size:5.5px;letter-spacing:2px;color:var(--muted);text-transform:uppercase;margin-top:3px}
  .welcome{position:absolute;left:22px;top:334px;right:20px}
  .welcome h1{font-family:"Cinzel",serif;font-weight:700;font-size:17.4px;line-height:23px;color:var(--text)}
  .bullets{list-style:none}
  .bullets li{position:relative;padding-left:17px;font-size:7.4px;line-height:9.6px;color:var(--text)}
  .bullets li::before{content:"";position:absolute;left:3px;top:3px;width:4px;height:4px;background:var(--text);transform:rotate(45deg)}
  .welcome .bullets{margin-top:12px}
  .welcome .bullets li{margin-bottom:10.2px}
  .strip{position:absolute;left:0;top:17px;display:block}
  .content{position:absolute;left:24px;right:24px;top:140px}
  .section{margin-bottom:9px}
  .section-head{display:flex;align-items:center;gap:11px;padding-bottom:4px;width:200px;border-bottom:1px solid var(--rule);margin-bottom:8px}
  .section-head svg{flex:none}
  .section-head h2{font-family:"Cinzel",serif;font-weight:700;font-size:14.5px;letter-spacing:.4px}
  .section .bullets{padding-left:8px}
  .section .bullets li{margin-bottom:10px}
  .summary{position:absolute;left:15px;right:15px;top:456px}
  .summary-tab{position:relative;width:140px;height:17px;margin-left:25px}
  .summary-tab svg{position:absolute;left:0;top:0}
  .summary-tab span{position:relative;display:block;text-align:center;font-family:"Cinzel",serif;font-weight:700;font-size:14px;line-height:18px;color:var(--ink)}
  .summary-box{background:var(--box);color:var(--box-text);font-size:6.7px;line-height:9.2px;text-align:center;padding:8px 14px}
  .contact{position:absolute;left:0;right:0;top:534px;text-align:center;font-size:7.4px;color:var(--text)}
</style>
</head>
<body>
<main class="spread">

  <!-- Front side -->
  <section class="page page--front">
    <svg class="collage" width="420" height="324" viewBox="0 0 420 324">
      <defs>
        <linearGradient id="portraitTone" x1="0" y1="0" x2="1" y2="1">
          <stop offset="0" stop-color="#2a2a2a"/><stop offset=".55" stop-color="#4a4a4a"/><stop offset="1" stop-color="#161616"/>
        </linearGradient>
        <linearGradient id="hallTone" x1="0" y1="0" x2="1" y2="1">
          <stop offset="0" stop-color="#e8e3da"/><stop offset="1" stop-color="#9b7a55"/>
        </linearGradient>
        <linearGradient id="kitchenTone" x1="0" y1="0" x2="0" y2="1">
          <stop offset="0" stop-color="#eeeae4"/><stop offset="1" stop-color="#a57e58"/>
        </linearGradient>
        <linearGradient id="houseTone" x1="0" y1="0" x2="0" y2="1">
          <stop offset="0" stop-color="#7a7fa0"/><stop offset=".6" stop-color="#d8cfc2"/><stop offset="1" stop-color="#eeeeee"/>
        </linearGradient>
        <linearGradient id="coastTone" x1="0" y1="0" x2="0" y2="1">
          <stop offset="0" stop-color="#9a8fb4"/><stop offset=".5" stop-color="#e8b9a8"/><stop offset=".7" stop-color="#3d5670"/><stop offset="1" stop-color="#4f8a3a"/>
        </linearGradient>
        <linearGradient id="lodgeTone" x1="0" y1="0" x2="1" y2="1">
          <stop offset="0" stop-color="#7a4f2c"/><stop offset=".5" stop-color="#2b4f80"/><stop offset="1" stop-color="#b89b78"/>
        </linearGradient>
      </defs>
      <rect width="420" height="324" fill="#ffffff"/>
      <polygon points="0,0 269,0 312,121 242,211 0,211" fill="url(#portraitTone)" role="img" aria-label="Photographer holding a camera up to the eye"/>
      <polygon points="272,0 420,0 420,119 316,119" fill="url(#hallTone)" role="img" aria-label="Hallway with framed pictures and a wooden bench"/>
      <polygon points="317,122 420,122 420,211 246,211" fill="url(#kitchenTone)" role="img" aria-label="Bright kitchen and dining room with timber beams"/>
      <polygon points="0,214 177,214 177,323 0,323" fill="url(#houseTone)" role="img" aria-label="White farmhouse lit at dusk"/>
      <polygon points="180,214 244,214 316,323 180,323" fill="url(#coastTone)" role="img" aria-label="Dark clad house on a coastal cliff at sunset"/>
      <polygon points="247,214 420,214 420,323 319,323" fill="url(#lodgeTone)" role="img" aria-label="Timber lodge living room with large glass walls"/>
    </svg>

    <div class="brand">
      <div class="brand-name">Rowan Ashby</div>
      <div class="brand-role">Photographer</div>
    </div>

    <div class="welcome">
      <h1>Welcome to the<br>KLD Real Estate Photography<br>Editing and Support Service</h1>
      <ul class="bullets">
        <li>Take your real estate business to the next level by providing impressive real estate imagery that makes you stands out from the competition</li>
        <li>Omit the stress of trying to find a good photographer or managing an unreliable one and hence have more time to focus on other aspects of your business</li>
        <li>Showcase your listings with better quality and more impactful photographs than your competitors thereby increasing potential for a quick sale</li>
        <li>Great first impressions matter and you will achieve this by looking and feeling more professional. This will attract and retain more future clients.</li>
      </ul>
    </div>
  </section>

  <!-- Back side -->
  <section class="page page--back">
    <svg class="strip" width="420" height="111" viewBox="0 0 420 111">
      <defs>
        <linearGradient id="loungeTone" x1="0" y1="0" x2="1" y2="0">
          <stop offset="0" stop-color="#3a3d45"/><stop offset="1" stop-color="#8a8c90"/>
        </linearGradient>
        <linearGradient id="bedroomTone" x1="0" y1="0" x2="1" y2="0">
          <stop offset="0" stop-color="#cfcfcf"/><stop offset=".6" stop-color="#f2f0ec"/><stop offset="1" stop-color="#d9d4cc"/>
        </linearGradient>
      </defs>
      <rect width="420" height="111" fill="#ffffff"/>
      <rect x="0" y="1" width="146" height="108" fill="url(#loungeTone)" role="img" aria-label="Dark living room with sofa and side table"/>
      <rect x="149" y="1" width="126" height="108" fill="var(--ink)" role="img" aria-label="Plain dark panel between the header photographs"/>
      <rect x="278" y="1" width="142" height="108" fill="url(#bedroomTone)" role="img" aria-label="Light bedroom opening onto a veranda"/>
    </svg>

    <div class="content">
      <div class="section">
        <div class="section-head">
          <svg width="15" height="17" viewBox="0 0 15 17"><rect x="1.5" y="1" width="12" height="15" fill="none" stroke="#f2f2f2" stroke-width="1"/><circle cx="7.5" cy="7" r="2.6" fill="none" stroke="#f2f2f2" stroke-width="1"/><line x1="4" y1="12.5" x2="11" y2="12.5" stroke="#f2f2f2" stroke-width="1"/></svg>
          <h2>How it works :</h2>
        </div>
        <ul class="bullets">
          <li>We understand that your time is valuable, so let us handle the editing and delivery of your images. You shoot, and we take care of the rest.</li>
          <li>Images are edited and delivered within 1 working day</li>
        </ul>
      </div>
      <div class="section">
        <div class="section-head">
          <svg width="15" height="17" viewBox="0 0 15 17"><rect x="3" y="1" width="9" height="7" fill="none" stroke="#f2f2f2" stroke-width="1"/><path d="M1 16 L4 9 L11 9 L14 16" fill="none" stroke="#f2f2f2" stroke-width="1"/><line x1="7.5" y1="9" x2="7.5" y2="16" stroke="#f2f2f2" stroke-width="1"/></svg>
          <h2>Inclusions :</h2>
        </div>
        <ul class="bullets">
          <li>Full day face to face training (we come to you) and instructional handbook</li>
          <li>We will teach you everything you need to know about your equipment and how to take stunning real estate photographs</li>
          <li>Service turnaround within 1 working day</li>
          <li>Free HELP desk service Mon-Fri</li>
          <li>12 month Exclusivity (rural towns only) for a limited time</li>
        </ul>
      </div>
      <div class="section">
        <div class="section-head">
          <svg width="17" height="17" viewBox="0 0 17 17"><rect x="1" y="6" width="6" height="10" fill="none" stroke="#f2f2f2" stroke-width="1"/><circle cx="12" cy="10" r="4" fill="none" stroke="#f2f2f2" stroke-width="1"/><line x1="3" y1="1" x2="3" y2="6" stroke="#f2f2f2" stroke-width="1"/></svg>
          <h2>Investment :</h2>
        </div>
        <ul class="bullets">
          <li>99 per listing for us to manage images including editing, quality control and delivery (10 Images)</li>
          <li>Ask us about competitive packages for photography equipment if required</li>
        </ul>
      </div>
    </div>

    <div class="summary">
      <div class="summary-tab">
        <svg width="140" height="17" viewBox="0 0 140 17"><polygon points="12,0 140,0 128,17 0,17" fill="var(--tab)"/></svg>
        <span>Summary</span>
      </div>
      <p class="summary-box">The KLD Real Estate Photography Editing and Support Service is the perfect solution for busy real estate professionals who want to take their business to the next level. Our service is affordable, flexible, and designed to help you showcase your listings in the best possible light.</p>
    </div>

    <p class="contact">Contact us today to learn more about how we can help you.</p>
  </section>

</main>
</body>
</html>
```